Business Card for Technology Startup

Design a 2-sided business card using the logo provided. We are a digital healthcare platform that provides a mobile app and web UI that helps caregivers, families, and doctors share information and provide better patient outcomes. We use AI and machine learning to help guide patients through their day-to-day life. The final design should communicate stability, peace, comfort, but also align with the image of an AI-driven technology startup.

I'd like the deliverable to by a Photoshop PSD file (with layers) that I can work with in pixlr.com. Should contain the following editable layers:
Name (ex. John Doe)
Title (ex. Founder / CEO)
Email (ex. info@brenvaxa.ai)
Phone (ex. (555) 014-2368)
Website (ex. https://brenvaxa.ai)

```html
<!DOCTYPE html>
<html lang="en">
<head>
<meta charset="utf-8">
<title>Brenvaxa Business Card</title>
<link rel="stylesheet" href="https://fonts.googleapis.com/css2?family=Poppins:wght@300;400;600&display=swap">
<style>
  :root {
    --backdrop: #9a9898;
    --card: #ffffff;
    --ink: #111111;
    --ink-soft: #1c2a3a;
    --accent-a: #1ec0ec;
    --accent-b: #6dcfdc;
  }
  html, body {
    margin: 0;
    padding: 0;
    width: 1199px;
    height: 1200px;
    overflow: hidden;
    background: var(--backdrop);
    font-family: "Poppins", sans-serif;
  }
  .canvas {
    position: relative;
    width: 1199px;
    height: 1200px;
  }
  .card {
    position: absolute;
    top: 157px;
    width: 519px;
    height: 883px;
    background: var(--card);
    overflow: hidden;
  }
  .card--front { left: 66px; }
  .card--back { left: 616px; }

  .brand {
    position: absolute;
    display: flex;
    align-items: center;
    gap: 18px;
  }
  .brand__dot {
    width: 42px;
    height: 42px;
    border-radius: 50%;
    background: linear-gradient(90deg, var(--accent-a), var(--accent-b));
    flex: none;
  }
  .brand__name {
    font-weight: 600;
    color: var(--ink);
    letter-spacing: 0.5px;
    line-height: 1;
    white-space: nowrap;
  }
  .card--front .brand { left: 62px; top: 130px; }
  .card--front .brand__name { font-size: 60px; }

  .person {
    position: absolute;
    left: 63px;
    top: 426px;
  }
  .person__name {
    margin: 0;
    font-size: 40px;
    font-weight: 600;
    color: var(--ink);
    line-height: 1.1;
  }
  .person__title {
    margin: 0;
    font-size: 21px;
    font-weight: 300;
    color: var(--ink);
  }

  .contacts {
    position: absolute;
    left: 62px;
    top: 575px;
    margin: 0;
    padding: 0;
    list-style: none;
  }
  .contacts__item {
    display: flex;
    align-items: center;
    gap: 14px;
    height: 40px;
    font-size: 21px;
    font-weight: 300;
    color: var(--ink-soft);
    white-space: nowrap;
  }
  .contacts__icon {
    width: 19px;
    height: 19px;
    fill: var(--accent-a);
    flex: none;
  }

  .accent-circle {
    position: absolute;
    border-radius: 50%;
    background: linear-gradient(90deg, var(--accent-a), var(--accent-b));
  }
  .card--front .accent-circle {
    left: 448px;
    top: 599px;
    width: 118px;
    height: 118px;
  }

  .card--back .accent-circle {
    left: 332px;
    top: 196px;
    width: 110px;
    height: 110px;
  }
  .card--back .brand__name {
    position: absolute;
    left: 77px;
    top: 468px;
    font-size: 66px;
  }
</style>
</head>
<body>
<main class="canvas">
  <section class="card card--front" aria-label="Card front">
    <div class="brand">
      <span class="brand__dot"></span>
      <span class="brand__name">brenvaxa</span>
    </div>

    <div class="person">
      <h1 class="person__name">John Doe</h1>
      <p class="person__title">Founder / CEO</p>
    </div>

    <ul class="contacts">
      <li class="contacts__item">
        <svg class="contacts__icon" viewBox="0 0 24 24" aria-hidden="true"><path d="M6.6 10.8a15.1 15.1 0 0 0 6.6 6.6l2.2-2.2a1 1 0 0 1 1-.25 11.4 11.4 0 0 0 3.6.57 1 1 0 0 1 1 1V20a1 1 0 0 1-1 1A17 17 0 0 1 3 4a1 1 0 0 1 1-1h3.5a1 1 0 0 1 1 1c0 1.25.2 2.45.57 3.570a1 1 0 0 1-.25 1z"/></svg>
        <span>(555) 014-2368</span>
      </li>
      <li class="contacts__item">
        <svg class="contacts__icon" viewBox="0 0 24 24" aria-hidden="true"><path d="M3 5h18a1 1 0 0 1 1 1v12a1 1 0 0 1-1 1H3a1 1 0 0 1-1-1V6a1 1 0 0 1 1-1zm1 2.3V17h16V7.3l-8 5.2z"/></svg>
        <span>info@brenvaxa.ai</span>
      </li>
      <li class="contacts__item">
        <svg class="contacts__icon" viewBox="0 0 24 24" aria-hidden="true"><path d="M12 2a10 10 0 1 0 0 20 10 10 0 0 0 0-20zm6.9 9h-3a15 15 0 0 0-1.3-5.9A8 8 0 0 1 18.9 11zM12 4c.9 1.2 1.8 3.6 1.9 7h-3.8c.1-3.4 1-5.8 1.9-7zM9.4 5.1A15 15 0 0 0 8.1 11h-3a8 8 0 0 1 4.3-5.9zM5.1 13h3a15 15 0 0 0 1.3 5.9A8 8 0 0 1 5.1 13zm6.9 7c-.9-1.2-1.8-3.6-1.9-7h3.8c-.1 3.4-1 5.8-1.9 7zm2.6-1.1a15 15 0 0 0 1.3-5.9h3a8 8 0 0 1-4.3 5.9z"/></svg>
        <span>brenvaxa.ai</span>
      </li>
    </ul>

    <div class="accent-circle"></div>
  </section>

  <section class="card card--back" aria-label="Card back">
    <div class="accent-circle"></div>
    <span class="brand__name">brenvaxa</span>
  </section>
</main>
</body>
</html>
```